Medical Centre Website

We need a new design for a medical centre based in Perth, Western Australia called 'Tarvin Grove Medical Centre'.

The medical centre does general practitioner work including general checkups, ecg, heart checks, woman's health and more servicing children and adults. They also do home visits on occasions where the patient cannot attend the centre.

They would like an information/brochure website where visitors can read up on the practice, send email and view their location.

The client wish the design to be clean, fresh and light. The main colours are a light purple/blue and to a dark navy blue. The client would not want the logo to be altered in any way. This includes changing the words colours or the image.

The final design should represent a loving, family friendly practice where patients can come to receive the best treatments.

We just need the end product to be presented to un in a layed psd format. The fonts must be as per the W3C standards.

**IMPORTANT**
I have received heaps of chatlink invites in the past. To treat everyone fairly, I do not add people to my chatlink list as in the past people expected us to give them the prize. If you have questions, please ask them in pixel forum as it may benefit others who are also designing the site. If I need to, I will send a message to the user.
Updates

Hi Designers,

Most designs we have received have been overly cluttered. Are you able to simplify the designs.

Cheers, Dorian

Hi Designers,

Some of the designs are quite attractive but aremore cluttered than I would like. If you have a look at the following design, the design is very simple and straight to the point. A lot of designs have too much wording and the reader can be put off. We are looking something more like:

velmoxa.com.au

I would prefer to see designs and have opened up the contest for a further 7 days.

Designers,

We have received feedback from the client and Quite frankly he don’t really like any of them.They are too cluttered and Americanised. All drab blue colours.
 
If you have a look at template monster, these designs are better and cleaner. We do not want heaps of writing on the front page.

If you look at the eariler examples such as quorbeyclinic.com.au which I did myself, the client loves that simplicity of the site.

```html
<!DOCTYPE html>
<html lang="en">
<head>
<meta charset="utf-8">
<title>Tarvin Grove Medical Centre</title>
<link rel="stylesheet" href="https://fonts.googleapis.com/css2?family=Source+Sans+3:wght@300;400;600;700&display=swap">
<style>
:root{
  --navy:#0c3c82;
  --navy-dark:#0a2f66;
  --nav-top:#1a78c8;
  --nav-bottom:#0b4a96;
  --hero-bg:#f3f3f3;
  --text:#3a3a3a;
  --muted:#6f6f6f;
  --icon:#555;
  --panel:#f4f4f4;
  --line:#e2e2e2;
  --white:#fff;
}
*{margin:0;padding:0;box-sizing:border-box}
html,body{width:890px;height:1200px;overflow:hidden;background:var(--white)}
body{position:relative;font-family:"Source Sans 3",sans-serif;color:var(--text)}
.abs{position:absolute}
.logo{left:96px;top:38px;font-weight:600;color:var(--navy);line-height:1}
.logo .name{display:block;font-size:28px}
.logo .sub{display:block;font-size:15px;letter-spacing:2.2px;text-transform:uppercase;margin-top:4px;padding-left:2px}
.phone{right:96px;top:66px;display:flex;align-items:center;gap:4px;font-weight:700;font-size:21px;color:var(--navy)}
.nav{left:0;top:102px;width:890px;height:48px;background:linear-gradient(var(--nav-top),var(--nav-bottom))}
.nav ul{list-style:none;display:flex;position:absolute;left:96px;top:0;height:48px}
.nav li{padding:0 15px;line-height:48px;font-weight:600;font-size:11.5px;color:var(--white);text-transform:uppercase}
.nav li.active{background:var(--navy-dark);padding:0 20px}
.brochure{right:95px;top:10px;width:136px;height:28px;background:#222;border:1px solid #444;display:flex;align-items:center;gap:7px;padding-left:6px;font-weight:600;font-size:10px;color:var(--white);text-transform:uppercase}
.brochure i{width:18px;height:20px;background:#fff;border-bottom:6px solid #c8231e}
.hero{left:0;top:150px;width:890px;height:298px;background:var(--hero-bg)}
.hero-photo{position:absolute;left:96px;top:0;width:352px;height:298px;background:linear-gradient(90deg,#e6e6e6,#dcdfe4 45%,#ececec)}
.hero-title{position:absolute;right:96px;top:100px;text-align:right;font-weight:300;font-size:35px;color:var(--navy);line-height:1}
.hero-sub{position:absolute;right:96px;top:145px;font-size:20px;letter-spacing:9.5px;color:#444;margin-right:-9px}
.btn-appoint{position:absolute;left:568px;top:186px;width:226px;height:38px;background:var(--navy);color:var(--white);font-weight:600;font-size:15px;text-transform:uppercase;text-align:center;line-height:38px}
.dots{position:absolute;right:96px;top:243px;display:flex;gap:3px}
.dots i{width:13px;height:13px;border-radius:50%;background:#666}
.dots i:first-child{background:var(--navy)}
h2{font-weight:700;font-size:15px;color:var(--navy);text-transform:uppercase}
.welcome{left:96px;top:480px;width:698px;text-align:center}
.welcome p{margin-top:14px;font-size:9px;line-height:17.8px;text-align:justify;text-align-last:center}
.services-title{left:0;top:622px;width:890px;text-align:center}
.service{top:666px;width:156px;text-align:center}
.service svg{display:block;margin:0 auto;height:64px}
.service p{margin-top:10px;font-size:9px;line-height:17.6px;text-align:justify;text-align-last:center}
.btn-small{display:inline-block;margin-top:12px;width:74px;height:25px;line-height:25px;background:var(--navy);color:var(--white);font-weight:600;font-size:9.5px;text-transform:uppercase}
.testimonials{left:96px;top:878px}
.avatar{left:99px;top:931px;width:103px;height:103px;border-radius:50%;background:radial-gradient(#6c6760,#3f3b38);border:4px solid #e9e9e9}
.quote-mark{left:204px;top:896px;font-family:Georgia,serif;font-size:32px;color:#444;font-weight:700}
.quote{left:218px;top:920px;width:280px;font-size:9.2px;line-height:17.8px;color:var(--muted);text-align:justify}
.quote-by{left:218px;top:1060px;font-weight:600;font-size:11px;color:#555}
.newsletter-title{left:510px;top:878px}
.newsletter{left:511px;top:906px;width:283px;height:188px;background:var(--panel);border:1px solid var(--line)}
.newsletter p{position:absolute;left:19px;top:12px;width:250px;font-size:9px;line-height:17.6px}
.field{position:absolute;left:19px;width:247px;height:29px;background:var(--white);font-size:8.5px;color:#999;line-height:29px;padding-left:12px}
.btn-sub{position:absolute;left:21px;top:143px;width:74px;height:26px;line-height:26px;text-align:center;background:var(--navy);color:var(--white);font-weight:700;font-size:9.5px;text-transform:uppercase}
.footer{left:0;top:1118px;width:890px;height:82px;background:var(--navy)}
.footer-links{position:absolute;left:101px;top:26px;font-size:11.5px;color:var(--white);word-spacing:1px}
.footer-links b{font-weight:400;margin:0 9px}
.copyright{position:absolute;left:96px;top:52px;font-size:11.5px;color:var(--white)}
.social{position:absolute;left:709px;top:29px;display:flex;gap:3px}
.social i{width:26px;height:26px;border-radius:50%;background:#2a7fd0;border:2px solid #fff}
.social i:last-child{background:#d63b30}
</style>
</head>
<body>

<header>
  <div class="abs logo"><span class="name">Tarvin Grove</span><span class="sub">Medical Centre</span></div>
  <div class="abs phone">
    <svg width="16" height="20" viewBox="0 0 16 20"><path d="M4 1l3 4-2 2c1 3 3 6 6 8l2-2 3 3-3 3C6 18 1 10 1 4z" fill="#333"/></svg>
    1-800-514-7730
  </div>
</header>

<nav class="abs nav">
  <ul>
    <li class="active">Home</li><li>About Us</li><li>Appointments</li><li>Patients</li><li>Services</li><li>FAQ's</li><li>Contact Us</li>
  </ul>
  <div class="abs brochure"><i></i>Download Broucher</div>
</nav>

<section class="abs hero">
  <div class="hero-photo" role="img" aria-label="Photo of a smiling doctor in a white coat with a family standing behind him"></div>
  <div class="hero-title">Tarvin Grove</div>
  <div class="hero-sub">Medical Centre</div>
  <div class="btn-appoint">Make an Appointment</div>
  <div class="dots"><i></i><i></i><i></i><i></i></div>
</section>

<section class="abs welcome">
  <h2>Welcome to Tarvin Grove Medical Centre</h2>
  <p>Lorem Ipsum is simply dummy text of the printing and typesetting industry. Lorem Ipsum has been the industry's standard dummy text ever since the 1500s, when an unknown printer took a galley of type and scrambled it to make a type specimen book. It has survived not only five centuries, but also the leap into electronic typesetting, remaining essentially unchanged. It was popularised in the 1960s with the release of Inkwell sheets containing Lorem Ipsum passages, and more recently with desktop publishing software like Folio Press including versions of Lorem Ipsum.</p>
</section>

<h2 class="abs services-title">Our Services</h2>

<div class="abs service" style="left:100px">
  <svg viewBox="0 0 40 70" width="37"><path d="M8 6v14c0 10 16 10 16 0V6M16 30v18c0 10 14 10 14 0v-8" fill="none" stroke="#555" stroke-width="3"/><circle cx="30" cy="36" r="5" fill="none" stroke="#555" stroke-width="3"/></svg>
  <p>Lorem Ipsum is simply dummy text of the printing and typesetting industry. Lorem Ipsum has been the industry's ...</p>
  <span class="btn-small">Read More</span>
</div>
<div class="abs service" style="left:276px">
  <svg viewBox="0 0 60 70" width="55"><path d="M2 35h18l4-8 5 20 5-26 4 14h20" fill="none" stroke="#555" stroke-width="3" stroke-linejoin="round"/></svg>
  <p>Lorem Ipsum is simply dummy text of the printing and typesetting industry. Lorem Ipsum has been the industry's ...</p>
  <span class="btn-small">Read More</span>
</div>
<div class="abs service" style="left:456px">
  <svg viewBox="0 0 50 70" width="46"><path d="M25 56C10 44 2 36 2 25 2 16 8 11 14 11c5 0 9 3 11 7 2-4 6-7 11-7 6 0 12 5 12 14 0 11-8 19-23 31z" fill="#555"/><path d="M4 32h13l3-6 4 14 4-18 3 10h15" fill="none" stroke="#fff" stroke-width="2.5"/></svg>
  <p>Lorem Ipsum is simply dummy text of the printing and typesetting industry. Lorem Ipsum has been the industry's ...</p>
  <span class="btn-small">Read More</span>
</div>
<div class="abs service" style="left:633px">
  <svg viewBox="0 0 30 70" width="28"><circle cx="15" cy="7" r="6" fill="#555"/><path d="M9 15h12l6 22h-5l2 8h-5v20h-4V45h-1v20h-4V45H5l2-8H3z" fill="#555"/></svg>
  <p>Lorem Ipsum is simply dummy text of the printing and typesetting industry. Lorem Ipsum has been the industry's ...</p>
  <span class="btn-small">Read More</span>
</div>

<h2 class="abs testimonials">Testimonials</h2>
<div class="abs avatar" role="img" aria-label="Portrait photo of a smiling male patient"></div>
<div class="abs quote-mark">&ldquo;</div>
<p class="abs quote">Lorem Ipsum is simply dummy text of the printing and typesetting industry. Lorem Ipsum has been the industry's standard dummy text ever since the 1500s, when an unknown printer took a galley of type and scrambled it to make a type specimen book. It has survived not only five centuries, but also the leap into electronic typesetting, remaining essentially unchanged. It was popularised in the 1960s with the release of Inkwell sheets containing ...&rdquo;</p>
<div class="abs quote-by">By Alden Rourke</div>

<h2 class="abs newsletter-title">Sign up for Newsletter</h2>
<div class="abs newsletter">
  <p>Lorem Ipsum is simply dummy text of the printing and typesetting industry. Lorem Ipsum has been the industry's ...</p>
  <div class="field" style="top:59px">Enter Name</div>
  <div class="field" style="top:101px">Enter E-mail ID</div>
  <div class="btn-sub">Subscribe</div>
</div>

<footer class="abs footer">
  <div class="footer-links">Home<b>|</b>About U<b>|</b>Appointments<b>|</b>Patients<b>|</b>Services<b>|</b>FAQ's<b>|</b>Contact Us</div>
  <div class="copyright">Copyright ©2013 Company Name &nbsp;- All rights reserved</div>
  <div class="social"><i></i><i></i><i></i></div>
</footer>

</body>
</html>
```